Pelmora Swifts Stridefair - 2 posters

We need two community event posters for an annual marathon with continuity in design showcasing the clubs logo colours and community spirit. Poster one is for the Juniors division which needs to look like a fun day encouraging families to come down and register and compete. It will be distributed to all the schools and social media. Poster two is for the main event again attracting registration with prizes. Encouraging all levels of runners from professionals to amateurs family friendly. It is in a unique location along the city's foreshore with amazing views.

Target Market(s)

Marathon runners, juniors, community and families

Requirements
Must have
• photos, logos details
Nice to have
• We are looking for a motivating high energy poster to entice registration and feel like fun event for the whole comminty

```html
<!DOCTYPE html>
<html lang="en">
<head>
<meta charset="utf-8">
<title>Swifts Junior Stridefair 2018</title>
<link href="https://fonts.googleapis.com/css2?family=Bebas+Neue&family=Montserrat:wght@600;700&family=Merriweather:wght@400;700&display=swap" rel="stylesheet">
<style>
  :root {
    --orange: #ee7d2a;
    --teal: #16b3b8;
    --navy: #17345f;
    --ribbon: #1f5f9c;
    --ribbon-dark: #134571;
    --red: #d0161f;
    --ink: #1a1a1a;
    --page: #ffffff;
    --backdrop: #e6e6e6;
  }
  * { margin: 0; padding: 0; box-sizing: border-box; }
  html, body { width: 1200px; height: 1200px; overflow: hidden; background: var(--backdrop); }
  .poster {
    position: absolute; left: 182px; top: 10px;
    width: 836px; height: 1180px;
    background: var(--page);
    overflow: hidden;
  }
  .hero-photo {
    position: absolute; left: 0; top: 42px; width: 836px; height: 558px;
    background: linear-gradient(180deg,
      #2a5fd0 0%, #3a6fd8 10%, #eef2fa 24%, #ffffff 34%, #f7f3ef 44%,
      #d9a07f 52%, #c4563f 58%, #3d6fb0 64%, #e08a4c 70%, #4a5566 77%,
      #8e9a72 85%, #c9cfa6 93%, #f3f3ec 100%);
  }
  .event-name {
    position: absolute; left: 0; width: 836px; top: 168px;
    display: flex; justify-content: center; align-items: center; gap: 14px;
  }
  .event-name .name {
    font-family: 'Bebas Neue', sans-serif;
    font-size: 50px; line-height: 0.95; color: var(--orange);
    text-align: center; letter-spacing: 1px;
  }
  .event-name .mark { width: 64px; height: 64px; border-radius: 50%; background: var(--teal); }
  .ribbon { position: absolute; left: 104px; top: 440px; width: 600px; height: 222px; }
  .ribbon-text {
    font-family: 'Bebas Neue', sans-serif; font-size: 46px; fill: #fff; letter-spacing: 0.5px;
  }
  .date {
    position: absolute; left: 0; width: 836px; top: 657px; text-align: center;
    font-family: 'Bebas Neue', sans-serif; color: var(--teal); font-size: 62px; line-height: 1;
  }
  .date .year { color: var(--orange); font-size: 70px; }
  .venue {
    position: absolute; left: 0; width: 836px; top: 733px; text-align: center;
    font-family: 'Merriweather', serif; font-weight: 700; color: var(--red); font-size: 23px;
  }
  .start-time {
    position: absolute; left: 0; width: 836px; top: 765px; text-align: center;
    font-family: 'Merriweather', serif; font-weight: 700; color: var(--navy); font-size: 29px;
  }
  .race-table {
    position: absolute; left: 64px; top: 816px; width: 688px; height: 104px;
    border: 1.5px solid #333; border-radius: 8px; overflow: hidden;
    display: flex;
  }
  .race {
    display: flex; flex-direction: column; justify-content: center; align-items: center;
    font-family: 'Montserrat', sans-serif; font-weight: 700; font-size: 18px; line-height: 1.3;
  }
  .race-short, .race-long { background: var(--orange); color: #fff; width: 196px; }
  .race-mid { background: #fff; color: var(--ink); flex: 1; }
  .prizes {
    position: absolute; left: 0; width: 836px; top: 943px; text-align: center;
    font-family: 'Merriweather', serif; font-weight: 700; color: var(--red); font-size: 22px;
  }
  .register-note {
    position: absolute; left: 0; width: 836px; top: 975px; text-align: center;
    font-family: 'Merriweather', serif; font-weight: 700; color: var(--ink); font-size: 17px;
  }
  .register-url {
    position: absolute; left: 0; width: 836px; top: 1000px; text-align: center;
    font-family: 'Merriweather', serif; font-weight: 700; color: var(--ink); font-size: 22px; letter-spacing: 4px;
  }
  .sponsor-credits {
    position: absolute; left: 62px; width: 712px; top: 1043px; text-align: center;
    font-family: 'Merriweather', serif; color: #333; font-size: 9.6px; line-height: 13px;
  }
  .sponsor-row {
    position: absolute; left: 62px; width: 720px; top: 1118px; height: 40px;
    display: flex; justify-content: space-between; align-items: center;
    font-family: 'Montserrat', sans-serif; font-weight: 700; font-size: 15px;
  }
  .sponsor { display: flex; align-items: center; gap: 6px; color: var(--navy); }
  .sponsor-dot { width: 16px; height: 16px; border-radius: 50%; background: var(--teal); }
  .sponsor-box { background: #111; color: #fff; padding: 8px 12px; }
  .sponsor-box .name { color: #fff; }
  .footer-stripes { position: absolute; left: 0; top: 1166px; width: 836px; height: 14px; display: flex; gap: 6px; }
  .stripe { flex: 1; }
  .stripe.orange { background: var(--orange); }
  .stripe.teal { background: var(--teal); }
</style>
</head>
<body>
<main class="poster">
  <div class="hero-photo" role="img" aria-label="Photo of a crowd of children in colourful race bibs sprinting from a blue inflatable start arch across a grassy foreshore"></div>

  <div class="event-name">
    <span class="name">Pelmora Swifts<br>Stridefair</span>
    <span class="mark"></span>
  </div>

  <svg class="ribbon" viewBox="0 0 600 222">
    <polygon points="10,150 80,122 112,162 80,218" fill="var(--ribbon-dark)"/>
    <polygon points="590,150 520,122 488,162 520,218" fill="var(--ribbon-dark)"/>
    <path d="M58,70 Q300,-20 542,70 L530,165 Q300,90 70,165 Z" fill="var(--ribbon)"/>
    <path id="ribbonLine" d="M78,130 Q300,40 522,130" fill="none"/>
    <text class="ribbon-text" text-anchor="middle"><textPath href="#ribbonLine" startOffset="50%">2018 SWIFTS JUNIOR STRIDEFAIR</textPath></text>
  </svg>

  <div class="date">SATURDAY JUNE 30, <span class="year">2018</span></div>
  <div class="venue">Foreshore - Pelmora Yacht Club</div>
  <div class="start-time">Races start 4.00pm</div>

  <section class="race-table">
    <div class="race race-short"><span>1 mile (1.6km)</span><span>3-6 years old</span></div>
    <div class="race race-mid"><span>2 miles (3.2km)</span><span>7-11 years old</span></div>
    <div class="race race-long"><span>3 miles (4.8km)</span><span>12-16 years old</span></div>
  </section>

  <div class="prizes">Great prizes &amp; fun for the whole family</div>
  <div class="register-note">Don’t miss out register at</div>
  <div class="register-url">pelmorastridefair.com</div>

  <p class="sponsor-credits">Pelmora Swifts Club proudly presents this event to the Community with thanks to generous Sponsors, Partners and Volunteers including: Brightwire Electrical | The Runner's Step | Coastline Sparks | The Harbourview Suites | Toastie Hut | Marlow Jewellers | Core Ten | Pelmora Motors | Dana Whitcombe MLA | Cafe Arcadia | Fernleigh Naturopathics | Fuelpoint Co | Harbour Pharmacy | Sport Central | Stride Podiatry | Hollis &amp; Grant | Volunteer Rescue | Kestrel Homes | Sunport Print</p>

  <div class="sponsor-row">
    <div class="sponsor"><span class="sponsor-dot"></span><span class="name">City of Pelmora</span></div>
    <div class="sponsor"><span class="name">Brightwire Electrical</span></div>
    <div class="sponsor sponsor-box"><span class="name">Lumen Events</span></div>
    <div class="sponsor"><span class="name">Swifts</span></div>
    <div class="sponsor"><span class="name">Harborcare</span></div>
  </div>

  <div class="footer-stripes">
    <span class="stripe orange"></span><span class="stripe teal"></span><span class="stripe orange"></span><span class="stripe teal"></span><span class="stripe orange"></span>
  </div>
</main>
</body>
</html>
```